Personal Development Business needs a Business Card Design Project

We need a buiness card design for a new Personal Development business based in S. NSW in Australia called "Willow Path Onward. Our target market is to women who are looking to re-enter the workforce, or already be in the workforce at the middle management level. As a result of consultations their outcomes will be, but not exclusive to: increased confidence, increased self esteem and self awareness, work-life balance, time management, positive thinking.
Behind the scenes of coaching and mentoring will be a spiritual "bent".
Anticipate a beautiful candle as a possible background - showing success and shining - see attachment which came off Pixelmarket. Colours - Unsure until I see something that "grabs my attention". Not esoteric fluffy design but something that suggests safe, professional, supportive of personal journey without being too corporate.
Look forward to what you come up with.
Target Market(s)
Some designers have been requesting various bits of information.
Personal information. See attachment.
Two-sided please.
Gold lines at all four edges.
Many thanks
Ruth
Industry/Entity Type
Business
Look and feel
Each slider illustrates characteristics of the customer's brand and the style your logo design should communicate.

```html
<!DOCTYPE html>
<html lang="en">
<head>
<meta charset="utf-8">
<title>Willow Path Onward – Business Card</title>
<link rel="stylesheet" href="https://fonts.googleapis.com/css2?family=Questrial&family=Lato:wght@400;700&display=swap">
<style>
  :root {
    --paper: #ffffff;
    --ink: #111111;
    --card-edge: #555555;
    --dash: #222222;
    --bloom-deep: #8c2a78;
    --bloom-mid: #b0559c;
    --bloom-light: #e7cfd6;
  }
  html, body {
    margin: 0;
    padding: 0;
    width: 1200px;
    height: 1114px;
    overflow: hidden;
    background: var(--paper);
  }
  .canvas {
    position: relative;
    width: 1200px;
    height: 1114px;
  }
  .card {
    position: absolute;
    box-sizing: border-box;
    border: 1px solid var(--card-edge);
    background: var(--paper);
    overflow: hidden;
  }
  .card--front { left: 447px; top: 10px; width: 751px; height: 461px; }
  .card--back  { left: 446px; top: 486px; width: 750px; height: 462px; }

  .bloom-photo {
    position: absolute;
    top: 0;
    left: 0;
    height: 100%;
    background:
      radial-gradient(circle at 70% 50%, var(--bloom-mid) 0%, var(--bloom-deep) 35%, rgba(140,42,120,0.7) 60%, var(--bloom-light) 100%);
  }
  .card--front .bloom-photo { width: 178px; background:
      radial-gradient(circle at 10% 45%, var(--bloom-mid) 0%, var(--bloom-deep) 40%, var(--bloom-light) 100%); }
  .card--back .bloom-photo { width: 589px; background:
      radial-gradient(circle at 45% 57%, var(--bloom-mid) 0%, var(--bloom-deep) 30%, rgba(150,60,130,0.85) 60%, var(--bloom-light) 100%); }

  .guide-line {
    position: absolute;
    left: 0; top: 0;
  }

  .contact {
    position: absolute;
    left: 380px;
    top: 68px;
    font-family: "Lato", sans-serif;
    color: var(--ink);
  }
  .contact__name {
    font-weight: 700;
    font-size: 16.5px;
    letter-spacing: 0.3px;
    margin: 0 0 22px 0;
  }
  .contact__lines {
    font-size: 16px;
    line-height: 20px;
    margin: 0;
    letter-spacing: 0.2px;
  }
  .contact__notes {
    font-family: "Lato", sans-serif;
    font-style: italic;
    font-size: 8px;
    margin-top: 12px;
    display: flex;
    align-items: center;
    gap: 2px;
  }

  .tagline {
    position: absolute;
    font-family: "Questrial", sans-serif;
    font-size: 45px;
    color: var(--ink);
    white-space: nowrap;
    margin: 0;
    font-weight: 400;
  }
  .card--front .tagline { left: 190px; top: 392px; }
  .card--back .tagline {
    left: 710px;
    top: 231px;
    transform: translate(-50%, -50%) rotate(-90deg);
  }
</style>
</head>
<body>
<main class="canvas">
  <section class="card card--front" aria-label="Card front">
    <div class="bloom-photo" role="img" aria-label="Close-up photograph of a purple allium flower head"></div>
    <svg class="guide-line" width="751" height="461" aria-hidden="true">
      <polyline points="568,107 248,107 248,402" fill="none" stroke="var(--dash)" stroke-width="4" stroke-dasharray="14 8"/>
    </svg>
    <div class="contact">
      <p class="contact__name">Employer Name &amp; Nickname</p>
      <p class="contact__lines">
        Information<br>
        employer@willowpathonward.com<br>
        www.willowpathonward.com<br>
        00612345678
      </p>
      <div class="contact__notes">
        <svg width="10" height="10" viewBox="0 0 10 10" aria-hidden="true"><path d="M1 9 L8 2" stroke="#333" stroke-width="1.2"/></svg>
        notes
      </div>
    </div>
    <h1 class="tagline">Willow Path Onward</h1>
  </section>

  <section class="card card--back" aria-label="Card back">
    <div class="bloom-photo" role="img" aria-label="Close-up photograph of a purple allium flower head"></div>
    <p class="tagline">Willow Path Onward</p>
  </section>
</main>
</body>
</html>
```